Business Card Design Project

I have just chosen a logo and would now like this designed onto a business card for my hair salon. I would like it to be classy not to busy and have a wow factor when people look at them
Has to Include on card:
Logo Design
And business details below
Kellie-ann Drummond (owner)
0482 736 219
Rdw@vomblet.com.au
71 Willowmere Rise Corvin Cove
Logo is now attached please provide designs
Hair

```html
<!DOCTYPE html>
<html lang="en">
<head>
<meta charset="utf-8">
<title>Willowmere Hair Salon – Business Card</title>
<link rel="stylesheet" href="https://fonts.googleapis.com/css2?family=Cinzel:wght@400&family=Exo+2:wght@200;400&family=Arimo:wght@400;700&display=swap">
<style>
  :root {
    --backdrop-light: #e6e6e6;
    --backdrop-dark: #8c8c8c;
    --gold-light: #ffcd4f;
    --gold-mid: #f2b43a;
    --gold-deep: #d7870f;
    --red-bright: #e8080a;
    --red-deep: #9e0000;
    --band-orange: #d8641f;
    --ink-red: #b3120f;
    --label-red: #9c1408;
    --ink-dark: #111111;
    --white: #ffffff;
  }
  * { margin: 0; padding: 0; box-sizing: border-box; }
  html, body {
    width: 1200px;
    height: 1000px;
    overflow: hidden;
  }
  body {
    background: radial-gradient(ellipse at 45% 40%, var(--backdrop-light) 0%, #c4c4c4 55%, var(--backdrop-dark) 100%);
    position: relative;
  }
  .business-card {
    position: absolute;
    left: 69px;
    top: 205px;
    width: 1063px;
    height: 591px;
    overflow: hidden;
    background: linear-gradient(210deg, var(--gold-light) 0%, var(--gold-mid) 45%, var(--gold-deep) 100%);
  }
  .hair-artwork {
    position: absolute;
    left: 0;
    top: 0;
    width: 660px;
    height: 591px;
    background: linear-gradient(100deg, var(--red-deep) 0%, var(--red-bright) 45%, rgba(215, 135, 15, 0.6) 80%, rgba(242, 180, 58, 0) 100%);
  }
  .brand {
    position: absolute;
    left: 56px;
    top: 40px;
    width: 420px;
    text-align: center;
    font-family: "Cinzel", serif;
    font-weight: 400;
    color: var(--white);
    line-height: 1;
  }
  .brand-line-main {
    display: block;
    font-size: 62px;
    letter-spacing: 0;
  }
  .brand-line-sub {
    display: block;
    font-size: 50px;
    margin-top: 10px;
  }
  .brand-mark {
    display: block;
    width: 46px;
    height: 46px;
    margin: 18px auto 0;
    background: var(--white);
  }
  .owner-block {
    position: absolute;
    left: 645px;
    top: 114px;
    width: 418px;
  }
  .owner-label {
    font-family: "Exo 2", sans-serif;
    font-weight: 400;
    font-size: 25px;
    line-height: 1;
    color: var(--label-red);
    padding-left: 3px;
  }
  .owner-name-band {
    margin-top: 3px;
    height: 52px;
    background: var(--band-orange);
    display: flex;
    align-items: center;
    padding-left: 6px;
  }
  .owner-name {
    font-family: "Exo 2", sans-serif;
    font-weight: 400;
    font-size: 35px;
    color: var(--white);
  }
  .owner-phone {
    margin-top: -2px;
    text-align: right;
    padding-right: 34px;
    font-family: "Exo 2", sans-serif;
    font-weight: 200;
    font-size: 35px;
    letter-spacing: 1px;
    color: var(--ink-red);
  }
  .contact-details {
    position: absolute;
    right: 34px;
    top: 440px;
    text-align: right;
    font-family: "Arimo", sans-serif;
    font-size: 21px;
    line-height: 30px;
    color: var(--ink-dark);
  }
  .contact-key { font-weight: 700; }
</style>
</head>
<body>
  <div class="business-card">
    <div class="hair-artwork" role="img" aria-label="Flowing red and gold hair strands illustration"></div>

    <div class="brand">
      <span class="brand-line-main">WILLOWMERE</span>
      <span class="brand-line-sub">Hair Salon</span>
      <span class="brand-mark" role="img" aria-label="Salon logo mark"></span>
    </div>

    <div class="owner-block">
      <p class="owner-label">owner</p>
      <div class="owner-name-band">
        <p class="owner-name">Kellie-ann Drummond</p>
      </div>
      <p class="owner-phone">0482 736 219</p>
    </div>

    <div class="contact-details">
      <p><span class="contact-key">Email:</span> Rdw@vomblet.com.au</p>
      <p><span class="contact-key">Address:</span> 71 Willowmere Rise Corvin Cove</p>
    </div>
  </div>
</body>
</html>
```